Pain Seminar Flyer 8.5x11

We are having a FREE seminar on Pain for our Bootcamp members at our gym. We are looking for a great looking flyer with pictures and a design to draw people in. I have attached our logo, pictures of the 2 speakers and a Word document of the flyer information needed. PLEASE PLEASE make our head shots small and in a circle like the example flyer we attached but obviously make the flyer much much nicer than the example. Also we attached pic ideas about pain.
- This must be in PSD. format WITH LAYERS and fonts so we can edit the time or reuse the flyer.
- Size 8.5x11
- Attached info. with pics and logo (along with other pics of pain!)
Thank you!
Gym

```html
<!DOCTYPE html>
<html lang="en">
<head>
<meta charset="utf-8">
<title>Free Pain Seminar Flyer</title>
<link href="https://fonts.googleapis.com/css2?family=Roboto+Condensed:wght@300;400;700&display=swap" rel="stylesheet">
<style>
  :root {
    --blue: #2f7fcc;
    --blue-deep: #2a72ba;
    --orange: #c07a2c;
    --ink: #141414;
    --charcoal: #3e3f41;
    --paper: #ffffff;
    --backdrop: #d9d9d9;
  }
  * { box-sizing: border-box; margin: 0; padding: 0; }
  html, body { width: 1200px; height: 1200px; overflow: hidden; }
  body {
    background: var(--backdrop);
    font-family: "Roboto Condensed", "Arial Narrow", sans-serif;
    color: var(--ink);
  }
  .flyer {
    position: absolute; left: 160px; top: 32px;
    width: 880px; height: 1136px;
    background: var(--paper);
    overflow: hidden;
  }
  .gym-backdrop {
    position: absolute; left: 0; top: 240px; width: 880px; height: 600px;
    background: linear-gradient(180deg, #ffffff 0%, #eceeef 35%, #e2e4e6 70%, #dcdfe2 100%);
  }
  .abs { position: absolute; left: 0; width: 880px; text-align: center; }
  .brand { top: 52px; }
  .brand-name {
    font-weight: 700; font-size: 44px; letter-spacing: 2px; color: var(--ink); line-height: 1;
  }
  .brand-tagline {
    margin-top: 12px; font-weight: 700; font-size: 15px; letter-spacing: 3px; color: var(--ink);
  }
  .pain-questions {
    top: 192px; display: flex; justify-content: center; gap: 52px;
    font-weight: 700; font-size: 34px; line-height: 1;
  }
  .headline {
    top: 250px; font-weight: 700; font-size: 100px; color: var(--blue); line-height: 1;
  }
  .subhead {
    top: 340px; font-weight: 400; font-size: 67px; color: var(--orange); line-height: 1;
  }
  .reserve {
    top: 432px; font-weight: 400; font-size: 45px; line-height: 1;
  }
  .call {
    top: 480px; font-weight: 400; font-size: 45px; line-height: 1;
  }
  .phone {
    background: var(--blue); color: #fff; font-weight: 700; padding: 0 4px;
  }
  .limited {
    top: 533px; font-weight: 400; font-size: 25px; line-height: 1;
  }
  .event-detail {
    font-weight: 700; font-size: 28px; line-height: 1;
  }
  .event-detail .label, .event-detail .accent { color: var(--blue); }
  .date { top: 603px; }
  .time { top: 645px; }
  .speaker-band { position: absolute; left: 0; top: 770px; }
  .portrait-ring {
    position: absolute; width: 206px; height: 206px; border-radius: 50%;
    background: var(--blue); padding: 7px;
  }
  .portrait {
    width: 192px; height: 192px; border-radius: 50%; border: 4px solid #fff;
  }
  .portrait-a { background: radial-gradient(circle at 50% 40%, #c9a98a 0%, #8a7a52 55%, #4f6a3a 100%); }
  .portrait-b { background: radial-gradient(circle at 50% 40%, #d9a88a 0%, #b78466 50%, #d5d5d5 100%); }
  .speaker-name {
    top: 922px; width: auto; font-size: 26px; font-weight: 400; color: #fff; line-height: 1; text-align: left;
  }
  .speaker-name strong { font-weight: 700; }
  .topics {
    position: absolute; left: 0; top: 978px; width: 880px; height: 94px; display: flex;
  }
  .topic-col {
    flex: 0 0 auto; background: var(--charcoal); padding-top: 18px;
    display: flex; flex-direction: column; gap: 8px;
  }
  .topic-col.left { width: 451px; padding-left: 70px; }
  .topic-col.right { width: 429px; padding-left: 24px; background: #444547; }
  .topic { display: flex; align-items: center; gap: 10px; color: #fff; font-size: 24px; font-weight: 300; line-height: 1; }
  .footer {
    position: absolute; left: 0; top: 1076px; width: 880px; height: 60px;
    background: var(--orange); display: flex; align-items: center; padding-left: 100px; gap: 8px;
    color: #fff; font-size: 16px; font-weight: 400;
  }
  .footer .web { margin-left: 22px; }
</style>
</head>
<body>
<main class="flyer">
  <div class="gym-backdrop" role="img" aria-label="Faded black-and-white photo of a gym interior with weight racks"></div>

  <header class="abs brand">
    <div class="brand-name">STRIDEWELL BOOTCAMPS</div>
    <div class="brand-tagline">THE ULTIMATE FITNESS SOLUTION</div>
  </header>

  <div class="abs pain-questions"><span>BACK PAIN?</span><span>SHOULDER PAIN?</span><span>KNEE PAIN?</span></div>

  <h1 class="abs headline">FREE SEMINAR</h1>
  <h2 class="abs subhead">ON HOW TO STOP PAIN</h2>

  <p class="abs reserve">RESERVATIONS REQUIRED</p>
  <p class="abs call">CALL <span class="phone">555-014-7720</span> TODAY</p>
  <p class="abs limited">LIMITED SPACE SO DON’T WAIT TO SIGN UP</p>

  <p class="abs event-detail date"><span class="label">DATE : </span>THURSDAY, APRIL <span class="accent">13th</span></p>
  <p class="abs event-detail time"><span class="label">TIME : </span>7:30PM-9PM</p>

  <svg class="speaker-band" width="880" height="210" viewBox="0 0 880 210" aria-hidden="true">
    <polygon points="0,0 300,42 440,50 580,42 880,0 880,210 0,210" fill="var(--blue)"/>
  </svg>

  <div class="portrait-ring" style="left:160px; top:700px;">
    <div class="portrait portrait-a" role="img" aria-label="Head shot of speaker Daniel Porter"></div>
  </div>
  <div class="portrait-ring" style="left:514px; top:696px;">
    <div class="portrait portrait-b" role="img" aria-label="Head shot of speaker Marcus Hale"></div>
  </div>

  <p class="abs speaker-name" style="left:130px;"><strong>DANIEL PORTER,</strong> PT, DPT, OCS</p>
  <p class="abs speaker-name" style="left:470px;"><strong>MARCUS HALE,</strong> MS, CSCS, FMS</p>

  <section class="topics">
    <div class="topic-col left">
      <div class="topic"><svg width="22" height="22" viewBox="0 0 22 22" aria-hidden="true"><rect x="2" y="3" width="16" height="16" rx="3" fill="none" stroke="#4aa3e8" stroke-width="2.4"/><path d="M6 11l4 4 9-10" fill="none" stroke="#4aa3e8" stroke-width="2.6"/></svg>How to Get Out of Pain</div>
      <div class="topic"><svg width="22" height="22" viewBox="0 0 22 22" aria-hidden="true"><rect x="2" y="3" width="16" height="16" rx="3" fill="none" stroke="#4aa3e8" stroke-width="2.4"/><path d="M6 11l4 4 9-10" fill="none" stroke="#4aa3e8" stroke-width="2.6"/></svg>What to do When an Exercise Hurts</div>
    </div>
    <div class="topic-col right">
      <div class="topic"><svg width="22" height="22" viewBox="0 0 22 22" aria-hidden="true"><rect x="2" y="3" width="16" height="16" rx="3" fill="none" stroke="#4aa3e8" stroke-width="2.4"/><path d="M6 11l4 4 9-10" fill="none" stroke="#4aa3e8" stroke-width="2.6"/></svg>How Exercise Helps Pain</div>
      <div class="topic"><svg width="22" height="22" viewBox="0 0 22 22" aria-hidden="true"><rect x="2" y="3" width="16" height="16" rx="3" fill="none" stroke="#4aa3e8" stroke-width="2.4"/><path d="M6 11l4 4 9-10" fill="none" stroke="#4aa3e8" stroke-width="2.6"/></svg>Q &amp; A to Fine Extraordinary Health</div>
    </div>
  </section>

  <footer class="footer">
    <svg width="20" height="24" viewBox="0 0 20 24" aria-hidden="true"><path d="M10 1a8 8 0 0 0-8 8c0 6 8 14 8 14s8-8 8-14a8 8 0 0 0-8-8z" fill="none" stroke="#fff" stroke-width="2"/><circle cx="10" cy="9" r="3" fill="#fff"/></svg>
    <span>STRIDEWELL PERSONAL TRAINING STUDIO, 120 Elm St. Fairview, CO 80000</span>
    <svg class="web" width="24" height="24" viewBox="0 0 24 24" aria-hidden="true"><circle cx="12" cy="12" r="10" fill="none" stroke="#fff" stroke-width="1.8"/><ellipse cx="12" cy="12" rx="4.5" ry="10" fill="none" stroke="#fff" stroke-width="1.5"/><path d="M2 12h20M4 7h16M4 17h16" stroke="#fff" stroke-width="1.5"/></svg>
    <span>www.stridewellfit.com</span>
  </footer>
</main>
</body>
</html>
```